Documentary Feature Film Website

We need a simple website designed for our Feature Documentary Film "Keeper of Wuyang". The film is about Liu Bo, a man who has been voluntarily patrolling a bridge in Nanjing, China, saving people from throwing themselves into the murky waters below, at the most popular suicide spot in the world.

The home page should either be based on the poster, or include the poster in a creative and elegant way.

We would like to try to either have the poster image be the focus of the main page or the trailer. Either way, the trailer should probably be the first thing you click on. (trailer will be provided later and will be in 16:9 ratio)

We will have a synopsis page, filmmakers page, contact page, and news page... (but these could be cool as a pop up window)

The news page will have to be easily updatable.

Later we may need a page for any media coverage about the film. And of course any awards or distinctions that the film garners.

The filmmakers page should include these bio's:
Martin Feldcamp (Director, Producer)
Peter G. Ravallo (Director, Producer)
Kevin Zhao (Co-Producer)
Megan Talbrook (Editor)
Thomas Wendrick (Composer)

Martin is the guy with the sunglasses. Peter is the guy with the hat. Kevin Zhao is the Chinese guy. Megan and Thomas W do not have photos.

Industry/Entity Type

Media

Requirements
Must have
• Filmmaker photos should only go with the filmmakers page.
The website should look very clean. No clutter.

```html
<!DOCTYPE html>
<html lang="en">
<head>
<meta charset="utf-8">
<title>Keeper of Wuyang — Synopsis</title>
<link rel="stylesheet" href="https://fonts.googleapis.com/css2?family=Bebas+Neue&family=Source+Sans+3:wght@400;600&display=swap">
<style>
:root{
  --red:#f90000;
  --nav:#232323;
  --footer:#000;
  --white:#fff;
  --sky-top:#b9b9b9;
  --sky-mid:#a9a9a9;
  --water:#7d7c78;
  --still-sky:#b4b4b2;
  --still-water:#6f6e6a;
  --heading:"Bebas Neue", Impact, sans-serif;
  --body:"Source Sans 3", "Myriad Pro", Arial, sans-serif;
}
*{box-sizing:border-box;margin:0;padding:0}
html,body{width:1200px;height:998px;overflow:hidden;background:var(--footer)}
.page{position:relative;width:1200px;height:998px;font-family:var(--body);color:var(--white)}

.hero{position:absolute;left:0;top:0;width:1200px;height:375px}
.hero-photo{position:absolute;inset:0;background:linear-gradient(180deg,var(--sky-top) 0%,var(--sky-mid) 60%,#8e8d88 78%,var(--water) 100%),linear-gradient(90deg,transparent 55%,rgba(70,66,60,.45) 70%,rgba(70,66,60,.55) 100%);background-blend-mode:multiply}
.hero-title{position:absolute;left:292px;top:124px;font-family:var(--heading);font-size:70px;line-height:58px;letter-spacing:1px;font-weight:400}
.hero-title .accent{color:var(--red);margin-left:14px}
.hero-credit{position:absolute;left:292px;top:244px;font-family:var(--heading);font-size:27px;letter-spacing:.5px;font-weight:400}

.main-nav{position:absolute;left:0;top:375px;width:1200px;height:71px;background:var(--nav)}
.nav-links{list-style:none;position:absolute;top:33px;left:0;font-family:var(--heading);font-size:14px;letter-spacing:.3px}
.nav-links li{position:absolute;white-space:nowrap}
.nav-links .active{color:var(--red)}
.nav-links .active::after{content:"";position:absolute;left:4px;right:4px;top:21px;height:1px;background:var(--red)}
.social{position:absolute;left:776px;top:33px;display:flex;gap:8px;font-family:var(--heading);font-size:12px;letter-spacing:.3px}
.social span{display:flex;align-items:center;gap:4px;white-space:nowrap}
.social span::before{content:"";width:7px;height:7px;border-radius:50%;background:var(--red)}

.synopsis{position:absolute;left:0;top:446px;width:1200px;height:466px;background:var(--red)}
.section-title{position:absolute;left:0;width:1234px;top:10px;text-align:center;font-family:var(--heading);font-size:38px;font-weight:400}
.feature-label{position:absolute;left:300px;width:234px;top:104px;text-align:center;font-family:var(--heading);font-size:26px;font-weight:400}
.film-still{position:absolute;left:337px;top:169px;width:172px;height:172px;border-radius:50%;background:linear-gradient(180deg,var(--still-sky) 0%,#9e9d9a 55%,var(--still-water) 100%)}
.written{position:absolute;left:613px;top:72px;font-family:var(--heading);font-size:13px;letter-spacing:.3px;font-weight:400}
.copy{position:absolute;left:613px;width:334px;font-size:12.6px;line-height:13.5px}
.copy.p1{top:104px}
.copy.p2{top:266px;left:611px}
.copy.p3{top:353px;left:611px}

.site-footer{position:absolute;left:0;top:912px;width:1200px;height:86px;background:var(--footer)}
.site-footer p{position:absolute;left:0;width:1200px;top:36px;text-align:center;font-size:10px;font-weight:600}
</style>
</head>
<body>
<div class="page">
  <header class="hero">
    <div class="hero-photo" role="img" aria-label="Misty photograph of the great river bridge with its towers above the water"></div>
    <h1 class="hero-title">Keeper<br>of<span class="accent">Wuyang</span></h1>
    <p class="hero-credit">A film by , Martin Feldcamp , Peter G. Ravallo</p>
  </header>

  <nav class="main-nav">
    <ul class="nav-links">
      <li class="active" style="left:412px">Synopsis</li>
      <li style="left:470px">Trailer</li>
      <li style="left:524px">Filmmakers</li>
      <li style="left:606px">Bios</li>
      <li style="left:646px">News</li>
      <li style="left:690px">Contact</li>
    </ul>
    <div class="social">
      <span>Workhub</span><span>Friendly</span><span>Snapshot</span><span>Chirper</span>
    </div>
  </nav>

  <main class="synopsis">
    <h2 class="section-title">Synopsis /</h2>
    <h3 class="feature-label">Keeper of Wuyang</h3>
    <div class="film-still" role="img" aria-label="Round film still of the misty bridge over the river"></div>
    <p class="written">Written work &nbsp;!</p>
    <p class="copy p1">Lorem ipsum dolor sit amet, consectetur adipiscing elit. Aenean vel diam non neque iaculis sollicitudin. Nunc nec massa et risus iaculis interdum et sed mi. Nam viverra ac neque eu aliquet. Maecenas posuere, neque non vestibulum sodales, arcu diam interdum nulla, in molestie magna magna vitae justo. Aenean semper volutpat sapien eu porta. Etiam vestibulum pharetra risus vel ultricies. Phasellus tempus, enim sed gravida interdum, lorem ipsum auctor libero, ut ultrices dolor dolor at nulla. Integer viverra vitae velit eget tincidunt. Fusce tristique eros ac est mattis consequat.</p>
    <p class="copy p2">Lorem ipsum dolor sit amet, consectetur adipiscing elit. Aenean vel diam non neque iaculis sollicitudin. Nunc nec massa et risus iaculis interdum et sed mi. Nam viverra ac neque eu aliquet. Maecenas posuere, neque non vestibulum sodales, arcu diam interdum nulla, in molestie magna magna vitae justo.</p>
    <p class="copy p3">Lorem ipsum dolor sit amet, consectetur adipiscing elit. Aenean vel diam non neque iaculis sollicitudin. Nunc nec massa et risus iaculis interdum et sed mi. Nam viverra ac neque eu aliquet. Maecenas posuere, neque non vestibulum sodales, arcu diam interdum nulla, in molestie magna magna vitae justo.</p>
  </main>

  <footer class="site-footer">
    <p>© Copyright 2014 The Wuyang Filmmakers, All Rights Reserved.</p>
  </footer>
</div>
</body>
</html>
```